New business card, letter head, email signature and Portfolio for our Security company.

We are an Vantage security company that provides a top quality manpower services to protect high rise buildings, retail and all type of properties and would like a new business card/logo look.

- We would like the spot UV design.
- Matt black (double sided).
- We would like to incorporate a royal blue colour (feel free to experiment with it).
- Feel free to try different lengths with the card to make it stand out more than a normal business card.
- We would like the logo to be an eagle eye in the background (shines when card is tilted slightly in the background, either on the front, back or both sides of the card). Image attached as an example of eye shape (colour to be either black or royal blue).
- MARLOW VANTAGE GUARD AGENCY PTY. LTD. and MVGA to be placed on one side of the card and on the other side of the card to have;

- Name in slightly bigger font than the position (directly on the bottom on the name).
- Mobile number
- Email address
- Website email address
- PO BOX address

Can we please have the files in a format that we can edit.

Reason: I need to consult my business partner with the designs so far and will make a decision from there.

Target Market(s)

Security Industry

Industry/Entity Type

Business

Contact Information for Business Card

- Mobile number
- Email address
- Website email address
- PO BOX address

Logo Text

MVGA and underneath the MVGA please add MARLOW VANTAGE GUARD AGENCY PTY. LTD.

Font styles to use
Other font styles liked:
• bold type font

Colors
0255a3
000000

Requirements
Must have
• We are an Vantage security company that provides a top quality manpower services to protect high rise buildings, retail and all type of properties and would like a new business card/logo look.
• - We would like the spot UV design.
• - Matt black (double sided).
• - We would like to incorporate a royal blue colour (feel free to experiment with it).
• - Feel free to try different lengths with the card to make it stand out more than a normal business card.
• - We would like the logo to be an eagle eye in the background (shines when card is tilted slightly in the background, either on the front, back or both sides of the card). Image attached as an example of eye shape (colour to be either black or royal blue).
• - MARLOW VANTAGE GUARD AGENCY PTY. LTD. and MVGA to be placed on one side of the card and on the other side of the card to have;
• - Name in slightly bigger font than the position (directly on the bottom on the name).
• - Mobile number
• - Email address
• - Website email address
• - PO BOX address
• Can we please have the files in a format that we can edit.
Nice to have
• Feel free to try different lengths with the card to make it stand out more than a normal business card.
• Please find "URBAN JUNGLE" font attached and incorporate MVGA into the same style with building's inside the MVGA bold front also add MARLOW into the bottom part of the S and follow on E - Vantage on the bottom S - SECURITY on the bottom S - SERVICES on the bottom of each letter.
• other than that, I'll be happy with a bold modern font for the MVGA and MARLOW VANTAGE GUARD AGENCY in a bold and thinner font underneath.

```html
<!DOCTYPE html>
<html lang="en">
<head>
<meta charset="utf-8">
<title>MVGA Business Card</title>
<link href="https://fonts.googleapis.com/css2?family=Black+Ops+One&family=Didact+Gothic&display=swap" rel="stylesheet">
<style>
  :root {
    --ink: #000000;
    --royal: #0255a3;
    --paper-light: #ffffff;
    --paper-edge: #dcdcdc;
    --divider: #111111;
  }
  * { margin: 0; padding: 0; box-sizing: border-box; }
  html, body { width: 1050px; height: 1200px; overflow: hidden; }
  body { position: relative; background: var(--paper-edge); }

  .card-face {
    position: absolute;
    left: 0;
    width: 1050px;
    background: radial-gradient(ellipse at 50% 50%, var(--paper-light) 0%, #f1f1f1 40%, var(--paper-edge) 100%);
  }
  .card-face--front { top: 0; height: 598px; }
  .card-face--back { top: 600px; height: 600px; }

  .divider {
    position: absolute;
    left: 0; top: 597px;
    width: 1050px; height: 2px;
    background: var(--divider);
  }

  .wordmark {
    position: absolute;
    font-family: "Black Ops One", system-ui, sans-serif;
    color: var(--ink);
    line-height: 1;
    text-align: center;
  }
  .wordmark__initials { display: block; }
  .wordmark__name { display: block; white-space: nowrap; }

  .wordmark--small { left: 60px; top: 58px; width: 380px; }
  .wordmark--small .wordmark__initials { font-size: 132px; letter-spacing: 2px; }
  .wordmark--small .wordmark__name { font-size: 19px; margin-top: 10px; letter-spacing: 0.5px; }

  .wordmark--large { left: 225px; top: 770px; width: 600px; }
  .wordmark--large .wordmark__initials { font-size: 214px; letter-spacing: 4px; }
  .wordmark--large .wordmark__name { font-size: 29px; margin-top: 16px; letter-spacing: 0.5px; }

  .contact-block {
    position: absolute;
    right: 54px;
    top: 262px;
    text-align: right;
  }
  .contact-block__name {
    font-family: "Black Ops One", system-ui, sans-serif;
    font-size: 48px;
    line-height: 1;
    color: var(--royal);
  }
  .contact-block__position {
    font-family: "Black Ops One", system-ui, sans-serif;
    font-size: 23px;
    line-height: 1;
    color: var(--ink);
    margin-top: 2px;
  }
  .contact-block__details {
    list-style: none;
    margin-top: 30px;
    font-family: "Didact Gothic", system-ui, sans-serif;
    font-size: 25px;
    line-height: 34px;
    color: var(--ink);
  }
</style>
</head>
<body>
  <section class="card-face card-face--front">
    <div class="wordmark wordmark--small">
      <span class="wordmark__initials">MVGA</span>
      <span class="wordmark__name">MARLOW VANTAGE GUARD AGENCY</span>
    </div>

    <div class="contact-block">
      <div class="contact-block__name">JOHN DOE</div>
      <div class="contact-block__position">POSITION</div>
      <ul class="contact-block__details">
        <li>09XXXXXXXXX</li>
        <li>XXXX@email.com</li>
        <li>XXXX@email.com</li>
        <li>PO BOX Address</li>
      </ul>
    </div>
  </section>

  <div class="divider"></div>

  <section class="card-face card-face--back">
  </section>
  <div class="wordmark wordmark--large">
    <span class="wordmark__initials">MVGA</span>
    <span class="wordmark__name">MARLOW VANTAGE GUARD AGENCY</span>
  </div>
</body>
</html>
```